Business Card, Stationary with Shark Logo for Personal Injury Lawyer

I need business cards and stationery with a shark logo for my Personal Injury Law Practice. Has to have this written on it:
Martin K. Hollis
Injury Lawyer
The Corvell Building
718 Tandy Street
Providence, Rhode Island 02908
401-627-4193
Martinhollis.com

Contact Information for Business Card

Martin K. Hollis, Injury Lawyer, address, 401-627-4193, martinhollis.com

```html
<!DOCTYPE html>
<html lang="en">
<head>
<meta charset="utf-8">
<title>Martin K. Hollis – Business Card</title>
<link href="https://fonts.googleapis.com/css2?family=Open+Sans:wght@400;700;800&display=swap" rel="stylesheet">
<style>
  :root {
    --navy: #2a2563;
    --ink-grey: #6b6b72;
    --paper: #ffffff;
    --backdrop: #e4e4e6;
  }
  * { margin: 0; padding: 0; box-sizing: border-box; }
  html, body {
    width: 1200px; height: 801px; overflow: hidden;
    background: var(--backdrop);
    font-family: "Open Sans", sans-serif;
  }
  .sheet {
    position: relative; width: 1200px; height: 801px;
    display: flex; align-items: center; justify-content: center; gap: 40px;
  }
  .card {
    width: 520px; height: 297px; position: relative;
    box-shadow: 0 2px 6px rgba(0,0,0,.12);
  }
  .card--front { background: var(--paper); display: flex; align-items: center; }
  .card--back {
    background: var(--navy);
    display: flex; align-items: center; justify-content: center;
  }
  .brand {
    display: flex; align-items: center; gap: 10px;
    font-weight: 800; text-transform: uppercase; line-height: 1;
  }
  .brand__mark { display: block; background: currentColor; }
  .card--front .brand {
    width: 236px; justify-content: center; color: var(--navy);
    font-size: 22px; letter-spacing: .5px;
  }
  .card--front .brand__mark { width: 14px; height: 14px; }
  .card--back .brand { color: var(--paper); font-size: 40px; letter-spacing: 1px; }
  .card--back .brand__mark { width: 24px; height: 24px; }
  .divider {
    width: 1px; height: 150px; background: var(--navy);
  }
  .details { padding-left: 26px; font-size: 13px; line-height: 1.4; color: var(--ink-grey); }
  .details__name {
    color: var(--navy); font-weight: 700; font-size: 17px;
    text-transform: uppercase; letter-spacing: .3px; line-height: 1.2;
  }
  .details__role { margin-bottom: 10px; }
  .details__building { color: var(--navy); }
  .details__address { margin-bottom: 10px; }
  .contact { display: flex; align-items: center; gap: 7px; }
  .contact svg { width: 11px; height: 11px; fill: var(--navy); flex: none; }
</style>
</head>
<body>
<main class="sheet">
  <section class="card card--front">
    <div class="brand"><span class="brand__mark"></span>Martin K. Hollis</div>
    <div class="divider"></div>
    <div class="details">
      <p class="details__name">Martin K. Hollis</p>
      <p class="details__role">Injury Lawyer</p>
      <p class="details__building">The Corvell Building</p>
      <p>718 Tandy Street</p>
      <p class="details__address">Providence, Rhode Island 02908</p>
      <p class="contact">
        <svg viewBox="0 0 24 24" aria-hidden="true"><path d="M6.6 10.8a15.1 15.1 0 0 0 6.6 6.6l2.2-2.2a1 1 0 0 1 1-.25 11.4 11.4 0 0 0 3.6.57 1 1 0 0 1 1 1V20a1 1 0 0 1-1 1A17 17 0 0 1 3 4a1 1 0 0 1 1-1h3.5a1 1 0 0 1 1 1c0 1.25.2 2.45.57 3.57a1 1 0 0 1-.25 1z"/></svg>
        401-627-4193
      </p>
      <p class="contact">
        <svg viewBox="0 0 24 24" aria-hidden="true"><circle cx="12" cy="12" r="11"/></svg>
        Martinhollis.com
      </p>
    </div>
  </section>
  <section class="card card--back">
    <div class="brand"><span class="brand__mark"></span>Martin K. Hollis</div>
  </section>
</main>
</body>
</html>
```